Package Design - Disposable Face Towel

Hi,

We are needing assistance with graphic design on our box/carton/package.

The attached image that is white is our biggest competitor.

Our brand is "BRIGHT DEW LTD." Please see the logo we uploaded.

Oder we have in mind for front of box:

Logo
LARGE TOWELS
50 Count
Ultra Soft| 100% USDA Bio-Based|100% Eucalyptus Viscose | Vegan
BRIGHTDEWLTD.EXAMPLE

We like medium to dark blue on most of the box, with white and minimal hot pink or salmon. Something that is sharp, modern, and stands out from our competitors.

Box dimensions are: 6.25 x 5.25 x 4.75 inches

This will be 1 of many design projects.

Target Market(s)

Female Beauty Products

Font styles to use
Serif
Sans Serif

Colors
0054AA
0677BA
7BADD7
CADEEF
E8F1F8
EB3D1F
EC4F4E
F09395
F8D3D4
FCEDEE

Requirements
Must have
• Needs to look sharp and modern

```html
<!DOCTYPE html>
<html lang="en">
<head>
<meta charset="utf-8">
<title>Bright Dew Ltd. – XL Dewy Cloths carton dieline</title>
<link rel="stylesheet" href="https://fonts.googleapis.com/css2?family=Italiana&family=Montserrat:wght@400;500;600&display=swap">
<style>
  :root {
    --backdrop: #c9dce6;
    --navy: #314a66;
    --mist: #d6e3ec;
    --flap: #dae6ee;
    --white: #ffffff;
    --flora: #7f97b3;
    --flora-soft: #aabdd0;
  }
  * { margin: 0; padding: 0; box-sizing: border-box; }
  html, body { width: 781px; height: 1200px; overflow: hidden; }
  body { background: var(--backdrop); position: relative; font-family: "Montserrat", sans-serif; }

  .dieline {
    position: absolute;
    left: 16px; top: 300px;
    width: 1380px; height: 1110px;
    transform: scale(0.54);
    transform-origin: top left;
  }
  .dieline-shapes { position: absolute; inset: 0; width: 1380px; height: 1110px; }

  .brand-name {
    position: absolute;
    font-family: "Italiana", serif;
    font-size: 29px;
    line-height: 1;
    color: var(--white);
    white-space: nowrap;
  }
  .product-label {
    position: absolute;
    height: 26px;
    padding: 0 11px;
    background: var(--white);
    color: var(--navy);
    font-size: 16px;
    font-weight: 500;
    line-height: 26px;
    white-space: nowrap;
  }
  .feature-list {
    position: absolute;
    color: var(--white);
    font-size: 8.4px;
    line-height: 11px;
    letter-spacing: 0.1px;
    white-space: nowrap;
  }
  .info-heading {
    position: absolute;
    color: var(--white);
    font-size: 14px;
    font-weight: 600;
  }
  .info-body {
    position: absolute;
    width: 185px;
    color: var(--white);
    font-size: 8.2px;
    line-height: 9.6px;
  }
  .panel-footer {
    position: absolute;
    color: var(--navy);
    font-size: 13.5px;
    font-weight: 500;
    white-space: nowrap;
  }
  .centered-lockup {
    position: absolute;
    display: flex;
    flex-direction: column;
    align-items: center;
    gap: 12px;
  }
  .centered-lockup .brand-name,
  .centered-lockup .product-label { position: static; }
</style>
</head>
<body>
<main class="dieline" aria-label="Carton dieline for Bright Dew Ltd. XL Dewy Cloths">
  <svg class="dieline-shapes" viewBox="0 0 1380 1110">
    <g class="flaps" fill="var(--flap)">
      <path d="M7 390 L9 337 L327 337 L331 390 Z"/>
      <path d="M661 390 L663 337 L990 337 L993 390 Z"/>
      <path d="M993 60 L995 3 L1319 3 L1325 60 Z"/>
      <path d="M7 723 L331 723 L327 780 L9 780 Z"/>
      <path d="M661 723 L993 723 L990 780 L665 780 Z"/>
      <path d="M329 1053 L660 1053 L654 1110 L336 1110 Z"/>
      <path d="M1325 398 L1380 393 L1380 710 L1325 715 Z"/>
    </g>

    <rect class="panel-row" x="2" y="390" width="1323" height="333" fill="var(--navy)"/>
    <rect class="lid-panel" x="993" y="60" width="332" height="331" fill="var(--navy)"/>
    <rect class="base-panel" x="329" y="722" width="331" height="331" fill="var(--navy)"/>

    <path class="wave" fill="var(--mist)" d="M2 590 C50 560 100 568 150 610 C200 655 250 690 331 690 C420 690 520 665 600 625 C630 605 650 585 661 578 L661 723 L2 723 Z"/>
    <path class="wave" fill="var(--mist)" d="M661 590 C709 560 759 568 809 610 C859 655 909 690 993 690 C1080 690 1180 665 1260 625 C1290 605 1310 585 1325 578 L1325 723 L661 723 Z"/>

    <g role="img" aria-label="Botanical line illustration of leaves and berry sprigs">
      <path fill="var(--flora)" opacity="0.5" d="M200 723 C205 660 225 610 255 580 C285 620 305 670 315 723 Z"/>
    </g>
    <g role="img" aria-label="Botanical line illustration with flowers, leaves and berry sprigs">
      <path fill="var(--flora-soft)" opacity="0.75" d="M500 723 C510 660 545 610 600 575 C640 620 655 670 658 723 Z"/>
    </g>
    <g role="img" aria-label="Botanical line illustration of leaves and berry sprigs">
      <path fill="var(--flora)" opacity="0.5" d="M860 723 C865 660 885 610 915 580 C945 620 965 670 975 723 Z"/>
    </g>
    <g role="img" aria-label="Botanical line illustration with flowers, leaves and berry sprigs">
      <path fill="var(--flora-soft)" opacity="0.75" d="M1160 723 C1170 660 1205 610 1260 575 C1300 620 1318 670 1322 723 Z"/>
    </g>
    <g role="img" aria-label="Small leaf sprigs">
      <ellipse cx="445" cy="635" rx="10" ry="18" fill="var(--flora-soft)" opacity="0.8"/>
      <ellipse cx="1105" cy="635" rx="10" ry="18" fill="var(--flora-soft)" opacity="0.8"/>
      <ellipse cx="1040" cy="285" rx="10" ry="20" fill="var(--flora-soft)" opacity="0.8"/>
      <ellipse cx="1280" cy="180" rx="8" ry="16" fill="var(--flora-soft)" opacity="0.8"/>
      <ellipse cx="372" cy="875" rx="10" ry="20" fill="var(--flora-soft)" opacity="0.8"/>
      <ellipse cx="614" cy="800" rx="8" ry="16" fill="var(--flora-soft)" opacity="0.8"/>
    </g>

    <g class="bubbles" fill="var(--mist)">
      <circle cx="289" cy="500" r="3"/><circle cx="293" cy="524" r="8"/>
      <circle cx="38" cy="617" r="6" fill="var(--white)"/><circle cx="50" cy="648" r="2" fill="var(--white)"/>
      <circle cx="123" cy="688" r="6" fill="var(--white)"/><circle cx="108" cy="683" r="2" fill="var(--white)"/>
      <circle cx="622" cy="505" r="2"/><circle cx="637" cy="508" r="2"/><circle cx="626" cy="522" r="5"/>
      <circle cx="949" cy="500" r="3"/><circle cx="953" cy="524" r="8"/>
      <circle cx="698" cy="617" r="6" fill="var(--white)"/><circle cx="710" cy="648" r="2" fill="var(--white)"/>
      <circle cx="783" cy="688" r="6" fill="var(--white)"/><circle cx="768" cy="683" r="2" fill="var(--white)"/>
      <circle cx="1282" cy="505" r="2"/><circle cx="1297" cy="508" r="2"/><circle cx="1286" cy="522" r="5"/>
      <circle cx="1041" cy="167" r="12"/><circle cx="1035" cy="203" r="3"/>
      <circle cx="1269" cy="291" r="4"/><circle cx="1279" cy="322" r="12"/>
      <circle cx="376" cy="778" r="12"/><circle cx="371" cy="812" r="3"/>
      <circle cx="604" cy="901" r="4"/><circle cx="616" cy="933" r="12"/>
    </g>
  </svg>

  <h2 class="info-heading" style="left:30px; top:466px;">Lorem Ipsum</h2>
  <p class="info-body" style="left:30px; top:489px;">Lorem ipsum dolor sit amet, consectetur adipiscing elit, sed do eiusmod tempor incididunt ut labore et dolore magna aliqua. Quis ipsum suspendisse ultrices gravida. Risus commodo viverra maecenas accumsan lacus vel facilisis.</p>
  <p class="panel-footer" style="left:32px; top:697px;">Brightdewltd.example</p>

  <p class="brand-name" style="left:360px; top:496px;">BRIGHT DEW LTD.</p>
  <p class="product-label" style="left:360px; top:533px;">XL Dewy Cloths</p>
  <p class="feature-list" style="left:361px; top:568px;">ULTRA GENTLE &nbsp;|&nbsp; PLANT-BASED FIBRE<br>SOFT EUCALYPTUS BLEND &nbsp;|&nbsp; CRUELTY-FREE</p>
  <p class="panel-footer" style="left:361px; top:697px;">50 Count</p>

  <h2 class="info-heading" style="left:692px; top:466px;">Lorem Ipsum</h2>
  <p class="info-body" style="left:692px; top:489px;">Lorem ipsum dolor sit amet, consectetur adipiscing elit, sed do eiusmod tempor incididunt ut labore et dolore magna aliqua. Quis ipsum suspendisse ultrices gravida. Risus commodo viverra maecenas accumsan lacus vel facilisis.</p>
  <p class="panel-footer" style="left:693px; top:697px;">Brightdewltd.example</p>

  <p class="brand-name" style="left:1020px; top:496px;">BRIGHT DEW LTD.</p>
  <p class="product-label" style="left:1020px; top:533px;">XL Dewy Cloths</p>
  <p class="feature-list" style="left:1021px; top:568px;">ULTRA GENTLE &nbsp;|&nbsp; PLANT-BASED FIBRE<br>SOFT EUCALYPTUS BLEND &nbsp;|&nbsp; CRUELTY-FREE</p>
  <p class="panel-footer" style="left:1021px; top:697px;">50 Count</p>

  <div class="centered-lockup" style="left:993px; width:332px; top:214px;">
    <p class="brand-name">BRIGHT DEW LTD.</p>
    <p class="product-label">XL Dewy Cloths</p>
  </div>

  <div class="centered-lockup" style="left:329px; width:331px; top:826px;">
    <p class="brand-name">BRIGHT DEW LTD.</p>
    <p class="product-label">XL Dewy Cloths</p>
  </div>
</main>
</body>
</html>
```